Vellorane- Comprehensive quality healthcare delivered at your door.

I am looking for brochures to help promote my business. My business name is Vellorne (see attachment and logo). This is a new health delivery system designed to provide high quality care to elderly in their communities or at home.

See attachements. The logo is already designed.

As far as services provided (see attachment)

Target Market(s)

Elderly patients

Industry/Entity Type

Business

Font styles to use
Serif

Colors

Designer to choose colors to be used in the design.

```html
<!DOCTYPE html>
<html lang="en">
<head>
<meta charset="utf-8">
<title>Vellorne Brochure</title>
<link href="https://fonts.googleapis.com/css2?family=Open+Sans:wght@400;600;700&family=Montserrat:wght@700;800&family=Berkshire+Swash&display=swap" rel="stylesheet">
<style>
:root{
  --bg:#e9e8e4;
  --paper:#ffffff;
  --cover:#f1f1ef;
  --green-light:#6a8a23;
  --green:#4f6d17;
  --green-dark:#3a540f;
  --orange:#e8890f;
  --ink:#2c2c2c;
  --on-green:#f3f5ea;
  --photo-a:#b79f83;
  --photo-b:#6d7c63;
}
*{box-sizing:border-box;margin:0;padding:0}
html,body{width:1200px;height:1013px;overflow:hidden;background:var(--bg)}
.canvas{position:relative;width:1200px;height:1013px}
.brochure{position:absolute;left:60px;top:96px;width:1080px;height:820px;display:flex;box-shadow:0 12px 40px rgba(0,0,0,.18)}
.panel{position:relative;width:360px;height:820px;overflow:hidden;font-family:"Open Sans",sans-serif}

/* Left panel */
.panel-about{background:var(--paper);color:var(--ink)}
.about-text{position:relative;z-index:1;padding:36px 30px 0 30px;font-size:13px;line-height:1.45}
.about-text p{margin-bottom:16px}
.about-photo{position:absolute;left:0;right:0;top:500px;bottom:72px;background:linear-gradient(170deg,#ffffff 0%,var(--photo-a) 30%,var(--photo-b) 100%)}
.call-band{position:absolute;left:0;right:0;bottom:0;height:72px;background:linear-gradient(90deg,var(--green-dark),var(--green-light));color:var(--on-green);font-family:"Montserrat",sans-serif;font-weight:700;font-size:27px;display:flex;align-items:center;justify-content:center;letter-spacing:.5px}

/* Middle panel */
.panel-services{background:radial-gradient(ellipse at 40% 35%,var(--green-light) 0%,var(--green) 55%,var(--green-dark) 100%);color:var(--on-green)}
.tab{display:inline-block;background:var(--orange);color:#fff;font-family:"Montserrat",sans-serif;font-weight:800;font-size:17px;padding:7px 26px 7px 22px;border-radius:0 18px 18px 0;letter-spacing:.5px}
.tab-services{margin-top:40px}
.service-list{list-style:none;padding:18px 30px 0 34px;font-size:12.5px;line-height:1.4}
.service-list li{position:relative;padding-left:14px;margin-bottom:9px}
.service-list li::before{content:"";position:absolute;left:0;top:7px;width:4px;height:4px;border-radius:50%;background:var(--on-green)}
.contact{position:absolute;left:0;right:0;top:500px;text-align:center}
.contact .tab{border-radius:18px;padding:8px 28px}
.contact-list{list-style:none;margin-top:26px;font-size:14px;line-height:1.4}
.contact-list li{margin-bottom:20px}
.contact-list svg{display:block;margin:0 auto 6px}

/* Right panel */
.panel-cover{background:var(--cover)}
.brand{display:flex;align-items:center;justify-content:center;gap:12px;margin-top:56px}
.brand-mark{width:30px;height:30px;border-radius:50%;background:var(--green)}
.brand-name{font-family:"Open Sans",sans-serif;font-weight:600;font-size:26px;color:var(--green-dark);letter-spacing:1px}
.cover-title{text-align:center;margin-top:30px;font-family:"Berkshire Swash",cursive;font-size:50px;font-weight:400;color:var(--green)}
.cover-photo{position:absolute;left:0;right:0;top:250px;bottom:0;background:linear-gradient(160deg,#dfe3e2 0%,var(--photo-a) 40%,#7c6657 75%,#5c5a55 100%)}
</style>
</head>
<body>
<div class="canvas">
  <div class="brochure">
    <section class="panel panel-about">
      <div class="about-text">
        <p>Vellorne offers home and Community Based Services for adults who wish to continue to live independently in the comfort of their communities.</p>
        <p>We provide on site services and deliver high quality healthcare at your door. Our experienced physicians coordinate care with our certified nurse practitioners and provide chronic care management, physical therapy, rehabilitation and medications management.</p>
        <p>Lorem Ipsum is simply dummy text of the printing and typesetting industry. Lorem Ipsum has been the industry's standard dummy text ever since the 1500s, when an unknown printer took a galley of type and scrambled it to make a type specimen book. It has survived not only five centuries, but also the leap into electronic typesetting, remaining essentially unchanged. It was popularised in the 1960s with the release of Letraset sheets containing Lorem Ipsum passages</p>
      </div>
      <div class="about-photo" role="img" aria-label="Photo of a group of friends cheering outdoors beside a pickup truck"></div>
      <div class="call-band">CALL US 555-014-272</div>
    </section>

    <section class="panel panel-services">
      <div class="tab tab-services">SERVICES</div>
      <ul class="service-list">
        <li>Comprehensive primary care services</li>
        <li>Coordination of speciality care</li>
        <li>Chronic disease management such as COPD, Asthma, Diabetes mellitus, Heart disease like congestive heart failure, Alzheimer's dementia, etc...</li>
        <li>Transitional Care</li>
        <li>Skilled nursing visits for wound care, catheter care, ostomy</li>
        <li>Social services assessment</li>
        <li>Home health assistance</li>
        <li>Physical therapy</li>
        <li>Mental, dental health</li>
        <li>Transportation</li>
      </ul>
      <div class="contact">
        <div class="tab">CONTACT US</div>
        <ul class="contact-list">
          <li><svg width="12" height="14" viewBox="0 0 12 14"><path d="M6 1a4 4 0 0 0-4 4c0 3 4 8 4 8s4-5 4-8a4 4 0 0 0-4-4z" fill="none" stroke="currentColor" stroke-width="1.4"/><circle cx="6" cy="5" r="1.4" fill="currentColor"/></svg>18 Larkspur Ln.<br>Fairhaven, OR 97402</li>
          <li><svg width="14" height="14" viewBox="0 0 14 14"><circle cx="7" cy="7" r="6" fill="none" stroke="currentColor" stroke-width="1.2"/><path d="M5 4l1 2-1 1c.5 1 1 1.5 2 2l1-1 2 1-.5 1.5C7 10.5 3.5 7 4 4.5z" fill="currentColor"/></svg>555-014-272</li>
          <li><svg width="14" height="14" viewBox="0 0 14 14"><circle cx="7" cy="7" r="6" fill="none" stroke="currentColor" stroke-width="1.2"/><path d="M1 7h12M7 1c-3 3-3 9 0 12M7 1c3 3 3 9 0 12" fill="none" stroke="currentColor" stroke-width="1"/></svg>www.vellorne.com</li>
          <li><svg width="16" height="12" viewBox="0 0 16 12"><rect x="1" y="1" width="14" height="10" fill="currentColor"/><path d="M1 1l7 6 7-6" fill="none" stroke="#4f6d17" stroke-width="1.2"/></svg>info@vellorne.com</li>
        </ul>
      </div>
    </section>

    <section class="panel panel-cover">
      <div class="brand"><span class="brand-mark"></span><span class="brand-name">VELLORNE</span></div>
      <h1 class="cover-title">Stay Home</h1>
      <div class="cover-photo" role="img" aria-label="Photo of a cheerful group of young friends posing together in a city street"></div>
    </section>
  </div>
</div>
</body>
</html>
```